Business cards needed

[UPDATE] Source files for logo now uploaded!

Hi there

Looking for a quick turnaround on business cards. I need to be able to have them designed and printed before the weekend.

Each business card will be custom as each person has their own superhero! I've attached the heroes.

The cards need to say:

Bellquist Forge & Crew

Tom Halvik

'Zark' (hero name)

tom@hqz-mail.co

www.hqz-mail.co

Skype tomhalvik

@jq8

I've uploaded the source files for the logo! Thanks!

```html
<!DOCTYPE html>
<html lang="en">
<head>
<meta charset="utf-8">
<title>Bellquist Forge &amp; Crew — Business Cards</title>
<link rel="stylesheet" href="https://fonts.googleapis.com/css2?family=Quicksand:wght@400;500;600&display=swap">
<style>
  :root {
    --backdrop: #a9abb0;
    --card: #ffffff;
    --brand-red: #e8424b;
    --ink: #555459;
    --hero-red: #e02a2e;
    --hero-blue: #1f4a86;
    --hero-navy: #1a2f55;
  }
  * { box-sizing: border-box; margin: 0; padding: 0; }
  html, body {
    width: 1200px; height: 800px; overflow: hidden;
    background: var(--backdrop);
    font-family: "Quicksand", sans-serif;
  }
  .stage {
    position: relative; width: 1200px; height: 800px;
    display: flex; align-items: center; justify-content: center; gap: 60px;
  }
  .card {
    position: relative;
    width: 360px; height: 520px;
    background: var(--card);
    box-shadow: 0 6px 18px rgba(0,0,0,.22);
    overflow: hidden;
  }

  /* Front: hero artwork */
  .hero-art {
    position: absolute; left: 30px; right: 0; bottom: 0; height: 300px;
    background: linear-gradient(160deg, var(--hero-red) 0%, var(--hero-red) 45%, var(--hero-blue) 75%, var(--hero-navy) 100%);
    clip-path: polygon(25% 0, 75% 8%, 100% 45%, 100% 100%, 0 100%, 5% 40%);
  }

  /* Back: brand and contacts */
  .card-back {
    display: flex; flex-direction: column; align-items: center;
    padding-top: 70px; border-bottom: 6px solid var(--brand-red);
  }
  .brand-mark {
    display: flex; align-items: center; gap: 10px;
    color: var(--brand-red); font-weight: 600; font-size: 19px;
  }
  .brand-mark .brand-square {
    width: 22px; height: 22px; background: var(--brand-red);
  }
  .company-name {
    margin-top: 16px; font-size: 16px; color: var(--ink); letter-spacing: .5px;
  }
  .person-name {
    margin-top: 30px; font-size: 27px; color: var(--ink); letter-spacing: .5px;
  }
  .hero-name {
    margin-top: 2px; font-size: 17px; color: var(--brand-red);
  }
  .contact-list {
    list-style: none; margin-top: 26px;
    display: flex; flex-direction: column; align-items: center; gap: 14px;
  }
  .contact-item {
    display: flex; flex-direction: column; align-items: center; gap: 5px;
    font-size: 13px; color: var(--ink);
  }
  .contact-icon { width: 20px; height: 20px; display: block; }
</style>
</head>
<body>
<main class="stage">
  <section class="card card-front">
    <div class="hero-art" role="img" aria-label="Illustration of the superhero Zark in red and blue costume with cape"></div>
  </section>

  <section class="card card-back">
    <div class="brand-mark"><span class="brand-square"></span>Bellquist Forge &amp; Crew</div>
    <p class="company-name">Bellquist Forge &amp; Crew</p>
    <h1 class="person-name">Tom Halvik</h1>
    <p class="hero-name">Zark</p>
    <ul class="contact-list">
      <li class="contact-item">
        <svg class="contact-icon" viewBox="0 0 20 20" aria-hidden="true">
          <circle cx="10" cy="10" r="10" fill="var(--brand-red)"/>
          <rect x="5" y="6.5" width="10" height="7" fill="none" stroke="#fff" stroke-width="1.3"/>
          <polyline points="5,6.5 10,10.5 15,6.5" fill="none" stroke="#fff" stroke-width="1.3"/>
        </svg>
        tom@hqz-mail.co
      </li>
      <li class="contact-item">
        <svg class="contact-icon" viewBox="0 0 20 20" aria-hidden="true">
          <circle cx="10" cy="10" r="10" fill="var(--brand-red)"/>
          <circle cx="10" cy="10" r="5" fill="none" stroke="#fff" stroke-width="1.3"/>
          <ellipse cx="10" cy="10" rx="2.2" ry="5" fill="none" stroke="#fff" stroke-width="1.1"/>
          <line x1="5" y1="10" x2="15" y2="10" stroke="#fff" stroke-width="1.1"/>
        </svg>
        www.hqz-mail.co
      </li>
      <li class="contact-item">
        <svg class="contact-icon" viewBox="0 0 20 20" aria-hidden="true">
          <circle cx="10" cy="10" r="10" fill="var(--brand-red)"/>
        </svg>
        tomhalvik
      </li>
      <li class="contact-item">
        <svg class="contact-icon" viewBox="0 0 20 20" aria-hidden="true">
          <circle cx="10" cy="10" r="10" fill="var(--brand-red)"/>
        </svg>
        @jq8
      </li>
    </ul>
  </section>
</main>
</body>
</html>
```